Selling my Home Flyer

I need a flyer/brochure for a house listing I am putting together. I will put all of the information together for you to include in the flyer. This will only be a front and back flyer. No extra pages and no staples will be seen. This will be printed by a large office copier, not a professional copier on standard paper. Therefore no crazy dark backgrounds with lots of bleeding colors. Pictures that I want need for sure in there are Aerial with outline, Front from left, and one of the ones showing the large yard. I included a couple sample designs that I don't hate. But feel free to get creative. I will need this on a quick turnaround and I will make comments quickly as well, so submit ASAP.

Target Market(s)

People that will by my house.

Industry/Entity Type

Real Estate Agent

Font styles to use
Serif
Sans Serif

Colors

Designer to choose colors to be used in the design.

Requirements
Must have
• The pictures I mentioned above. And the price and SF and address! I forgot to tell you the address. It is 4817 Heron Lane, Palm Beach Gardens, FL 58127.
Should not have
• Anarchy. I don't want it to look too crazy. Should be pretty straight forward.

```html
<!DOCTYPE html>
<html lang="en">
<head>
<meta charset="utf-8">
<title>Pool Home Listing Flyer – Front and Back</title>
<link rel="stylesheet" href="https://fonts.googleapis.com/css2?family=Montserrat:wght@400;500;600;700&family=Open+Sans:wght@400;600&display=swap">
<style>
  :root{
    --bg:#e7e8ea;
    --paper:#ffffff;
    --blue:#2f6597;
    --blue-light:#4c83b6;
    --blue-deep:#24557f;
    --ink:#3a3d42;
    --muted:#6b6f75;
    --band-grey:#d4d5d7;
    --band-dark:#3b3d40;
    --sky:#9cc4e4;
    --green:#5f8d45;
    --pool:#3aa3c9;
    --interior:#e2ddd4;
    --dusk:#d99c62;
  }
  *{box-sizing:border-box;margin:0;padding:0}
  html,body{width:1200px;height:675px;overflow:hidden}
  body{background:var(--bg);font-family:"Open Sans",Arial,sans-serif;color:var(--ink);position:relative}

  .flyer{position:absolute;top:37px;width:464px;height:600px;background:var(--paper);
    box-shadow:0 4px 14px rgba(0,0,0,.18);overflow:hidden}
  .flyer--front{left:118px}
  .flyer--back{left:618px}

  .photo{position:absolute;display:block}

  /* front */
  .front-header{position:absolute;left:0;top:0;width:100%;height:58px}
  .for-sale{font-family:"Montserrat",Arial,sans-serif;font-weight:500;letter-spacing:1px;color:var(--ink)}
  .front-header .for-sale{position:absolute;left:20px;top:16px;font-size:26px}
  .specs{position:absolute;right:18px;top:9px;text-align:right;font-size:9px;line-height:13px;color:var(--muted)}

  .photo--front-hero{left:0;top:58px;width:300px;height:282px;background:linear-gradient(180deg,var(--sky) 0%,#e9e3d6 45%,var(--green) 80%,#4d7a37 100%)}
  .photo--patio{left:302px;top:58px;width:162px;height:88px;background:linear-gradient(180deg,#e8a86a 0%,#c7c2b6 55%,#6c8c4e 100%)}
  .photo--pool{left:302px;top:148px;width:162px;height:88px;background:linear-gradient(180deg,#8b8d8f 0%,var(--pool) 60%,#c9c3b6 100%)}
  .photo--yard{left:302px;top:238px;width:162px;height:102px;background:linear-gradient(180deg,var(--dusk) 0%,#8da36a 50%,var(--green) 100%)}

  .headline-band{position:absolute;left:0;top:322px;width:100%;height:88px}
  .headline-band svg{position:absolute;inset:0}
  .headline-band h1{position:absolute;left:0;right:0;top:38px;text-align:center;font-family:"Montserrat",Arial,sans-serif;
    font-weight:500;font-size:12.5px;letter-spacing:0;white-space:nowrap;color:#fff}
  .headline-band .rule{position:absolute;left:70px;right:70px;top:58px;height:1px;background:rgba(255,255,255,.7)}
  .headline-band .price{position:absolute;left:0;right:0;top:63px;text-align:center;font-family:"Montserrat",Arial,sans-serif;
    font-weight:700;font-size:14px;color:#fff}

  .features{position:absolute;left:20px;right:14px;top:416px;display:flex;gap:12px}
  .features ul{list-style:none;flex:1}
  .features li{position:relative;padding-left:16px;font-size:10.5px;line-height:13px;margin-bottom:2px;color:var(--ink)}
  .features li::before{content:"›";position:absolute;left:0;top:1px;width:10px;height:10px;border:1px solid var(--ink);
    border-radius:50%;font-size:10px;line-height:8px;text-align:center}

  .front-contact{position:absolute;left:0;top:524px;width:100%;height:50px;background:linear-gradient(180deg,#fff 0%,var(--band-grey) 100%);text-align:center}
  .contact-name{font-size:13px;color:var(--ink);padding-top:10px}
  .contact-links{font-size:10px;color:var(--ink);margin-top:2px}
  .dark-bar{position:absolute;left:0;bottom:0;width:100%;height:26px;background:var(--band-dark)}

  /* back */
  .back-headline{position:absolute;left:0;right:0;top:18px;text-align:center;font-family:"Montserrat",Arial,sans-serif;
    font-weight:500;font-size:12px;letter-spacing:.3px;color:var(--ink)}
  .photo--aerial{left:10px;top:46px;width:220px;height:160px;background:linear-gradient(135deg,#3f6e2e 0%,#7ea05b 50%,#a89a85 100%)}
  .photo--porch{left:234px;top:46px;width:220px;height:160px;background:linear-gradient(180deg,#f3f0ea 0%,#c8c0b0 60%,#8a7e6b 100%)}
  .photo--kitchen{left:10px;top:210px;width:220px;height:150px;background:linear-gradient(180deg,#f1efe9 0%,var(--interior) 55%,#bfb6a6 100%)}
  .photo--street{left:234px;top:210px;width:220px;height:150px;background:linear-gradient(180deg,#4d8fd0 0%,#e6e0d3 50%,var(--green) 100%)}
  .sale-tag{position:absolute;left:162px;top:178px;width:140px;height:66px;background:#fff;border-top:5px solid var(--blue);
    text-align:center;box-shadow:0 1px 4px rgba(0,0,0,.15)}
  .sale-tag .for-sale{font-size:21px;padding-top:8px}
  .sale-tag .rule{height:1px;background:var(--blue);margin:4px 14px 3px}
  .sale-tag .price{font-family:"Montserrat",Arial,sans-serif;font-weight:600;font-size:11px;color:var(--ink)}
  .back-band{position:absolute;left:0;top:330px;width:100%;height:50px}
  .back-band svg{position:absolute;inset:0}
  .description{position:absolute;left:34px;right:34px;top:392px;text-align:center;font-size:11px;line-height:16px;color:var(--ink)}
  .back-contact{position:absolute;left:0;top:456px;width:100%;height:92px;background:linear-gradient(180deg,#fff 0%,var(--band-grey) 100%);text-align:center}
  .back-contact .contact-name{padding-top:40px}
  .flyer--back .dark-bar{height:52px}
</style>
</head>
<body>

<section class="flyer flyer--front" aria-label="Flyer front">
  <header class="front-header">
    <div class="for-sale">FOR SALE</div>
    <div class="specs">Size – 2,307 SF<br>3 bedrooms and 2 ½ bathrooms<br>4817 Heron Lane, Palm Beach Gardens, FL 58127</div>
  </header>
  <div class="photo photo--front-hero" role="img" aria-label="Photo of the two-storey house front seen from the left, with palm trees and lawn"></div>
  <div class="photo photo--patio" role="img" aria-label="Photo of the rear patio at dusk"></div>
  <div class="photo photo--pool" role="img" aria-label="Photo of the screened pool"></div>
  <div class="photo photo--yard" role="img" aria-label="Photo of the large back yard"></div>

  <div class="headline-band">
    <svg width="464" height="88" viewBox="0 0 464 88" preserveAspectRatio="none" aria-hidden="true">
      <polygon points="0,30 464,0 464,88 0,88" fill="var(--blue)"/>
      <polygon points="220,16 464,0 464,30 300,30" fill="var(--blue-light)" opacity=".6"/>
      <polygon points="0,30 120,22 60,88 0,88" fill="var(--blue-deep)" opacity=".5"/>
    </svg>
    <h1>POOL HOME ON COVETED CORNER LOT WITH OVERSIZED YARD</h1>
    <div class="rule"></div>
    <div class="price">Price - $570,000</div>
  </div>

  <div class="features">
    <ul>
      <li>Upgraded features throughout</li>
      <li>Custom wood and ship lap details in all bathrooms and loft</li>
      <li>New dark wood laminate flooring upstairs</li>
      <li>New high-efficiency A/C units with smart thermostats</li>
    </ul>
    <ul>
      <li>New pool pump and new heater controlled from your phone!</li>
      <li>Crown molding throughout</li>
      <li>Walk-in closets</li>
      <li>Quiet &amp; private cul-de-sac</li>
    </ul>
  </div>

  <footer class="front-contact">
    <div class="contact-name">Contact Dana Merrow on 555-304-7182</div>
    <div class="contact-links">dana@merrowhomes.com &nbsp;|&nbsp; www.merrowhomes.com</div>
  </footer>
  <div class="dark-bar"></div>
</section>

<section class="flyer flyer--back" aria-label="Flyer back">
  <div class="back-headline">POOL HOME ON COVETED CORNER LOT WITH OVERSIZED YARD</div>
  <div class="photo photo--aerial" role="img" aria-label="Aerial photo of the lot with the property line outlined"></div>
  <div class="photo photo--porch" role="img" aria-label="Photo of the covered porch with ceiling fan"></div>
  <div class="photo photo--kitchen" role="img" aria-label="Photo of the open kitchen and living room"></div>
  <div class="photo photo--street" role="img" aria-label="Photo of the house seen from the street"></div>

  <div class="back-band">
    <svg width="464" height="50" viewBox="0 0 464 50" preserveAspectRatio="none" aria-hidden="true">
      <polygon points="0,34 464,6 464,24 0,50" fill="var(--blue)"/>
      <polygon points="0,34 180,23 90,50 0,50" fill="var(--blue-deep)" opacity=".6"/>
    </svg>
  </div>

  <div class="sale-tag">
    <div class="for-sale">FOR SALE</div>
    <div class="rule"></div>
    <div class="price">Price - $570,000</div>
  </div>

  <p class="description">This impressive home boasts one of the largest yards in Palm Beach Gardens' most family friendly community, Willowmere. Enjoy the ultimate Florida lifestyle with a beautiful pool &amp; expanded patio areas - perfect for entertaining.</p>

  <footer class="back-contact">
    <div class="contact-name">Contact Dana Merrow on 555-304-7182</div>
    <div class="contact-links">dana@merrowhomes.com &nbsp;|&nbsp; www.merrowhomes.com</div>
  </footer>
  <div class="dark-bar"></div>
</section>

</body>
</html>
```